Brisk Tissu, wipes multipack branding 3 types in 1 family

Brisk Tissu is a wipe producing company. For some information see our (not completed) website at briskissu.nl. We also have a product named Palmora (see Palmora.com).
Our philosophy is to produce environmental friendly wipes only. We are doing that by using both bamboo and 100% bioviscose as Nonwoven. Both are biodegradable and compostable. We produce single packed wipes and multipacks (think about hygiene for hand, deodorant wipes and playtime wipes (for cleaning sex toys)). We are looking for designs for our multipacks (6 to 10 pieces per package). The size of the unfolded package foil is about 150 x 190mm (width x height) (but varies depending on the material and the number of wipes).
The branding should be modern, fresh and in line with our thoughts.

We want to have 3 packages designed for:
- Purely2Palms multipack 6 pieces
- Deodorant wipes multipack 6 pieces
- Playtime wipes multipack 10 pieces
All should have the look and feel of our Brisk Tissu logo / branding, and belong to the same family of products (to be recognised they belong together).

I added our logo as well as some examples of other packages we have been creating as samples. At first we have been thinking about using that design for multipacks as well, but we were not that happy about that.
Please consider them as a style that we liked.

Target Market(s)

Consumers
- Festival people (Purely2Palms and Deodorant)
- Adults with children (Purely2Palms)
- Travelers (Purely2Palm and Deodorant)
- Business people (Deodorant)
- Erotic industry (Playtime wipes)

Font styles to use
Sans Serif

Colors

Designer to choose colors to be used in the design.

Requirements
Must have
• A family in branding, recognisability as being part of 1 family of products.
• Branded with our logo (as attached).
• Necessary and mandatory information on the back of the package.
Nice to have
• Designs that fit to the purpose of the wipes.
• Different Colors for the different products.
• Chosen font is just because it is modern. Could be any other modern font as well.
Should not have
• Old fashioned style.
• Too much focus on the "green-ness" of the products.

```html
<!DOCTYPE html>
<html lang="en">
<head>
<meta charset="utf-8">
<title>Brisk Tissu – Deo Wipe for women</title>
<link href="https://fonts.googleapis.com/css2?family=Nunito+Sans:wght@300;400;800&family=Arimo:wght@400&display=swap" rel="stylesheet">
<style>
  :root {
    --backdrop: #e0eef6;
    --rose: #e95f80;
    --blush: #f5c1d3;
    --berry: #e5446a;
    --crimson: #d42a58;
    --ink: #1a1a1a;
    --white: #ffffff;
  }
  html, body { margin: 0; padding: 0; overflow: hidden; }
  body { width: 1012px; height: 1200px; background: var(--backdrop); position: relative; }
  .pack {
    position: absolute; left: 110px; top: 96px; width: 778px; height: 980px;
    background: var(--rose); overflow: hidden;
  }
  .pack-art { position: absolute; inset: 0; }
  .text { position: absolute; font-family: "Arimo", Arial, sans-serif; color: var(--ink); }
  .label { color: var(--crimson); font-size: 13px; line-height: 16px; }
  .intro { left: 111px; top: 110px; width: 570px; font-size: 12.2px; line-height: 16px; }
  .maker { left: 109px; top: 738px; width: 600px; font-size: 12.2px; line-height: 15px; }
  .best-before { left: 109px; top: 791px; font-size: 12.2px; }
  .ingredients { left: 109px; top: 862px; width: 620px; font-size: 10.5px; line-height: 14px; }
  .ingredients .label { color: var(--ink); font-size: 12.2px; }
  .brand-name {
    position: absolute; left: 244px; top: 328px; margin: 0;
    font-family: "Nunito Sans", sans-serif; font-weight: 800; font-size: 44px; line-height: 38px;
    color: var(--crimson); letter-spacing: 1px;
  }
  .tagline {
    position: absolute; left: 210px; top: 502px;
    font-family: "Nunito Sans", sans-serif; font-weight: 300; font-size: 21px; color: var(--white);
  }
  .product-name {
    position: absolute; left: 208px; top: 522px; margin: 0;
    font-family: "Nunito Sans", sans-serif; font-weight: 800; font-size: 76px; line-height: 76px;
    letter-spacing: -1px;
  }
  .product-name .deo { color: var(--blush); }
  .product-name .wipe { color: var(--crimson); margin-left: 18px; }
  .audience {
    position: absolute; left: 380px; top: 592px;
    font-family: "Nunito Sans", sans-serif; font-weight: 400; font-size: 32px; color: var(--crimson);
  }
  .seal-strip { position: absolute; left: 30px; top: 860px; width: 26px; height: 68px; background: var(--blush); }
</style>
</head>
<body>
  <section class="pack">
    <svg class="pack-art" width="778" height="980" viewBox="0 0 778 980">
      <rect class="right-panel" x="0" y="0" width="778" height="980" fill="var(--berry)"/>
      <path class="right-panel-texture" role="img" aria-label="diamond dot pattern on the right panel"
            d="M598,0 L778,0 L778,980 L442,980 C520,820 580,700 570,580 C560,470 440,440 435,330 C430,220 520,120 598,0 Z"
            fill="var(--crimson)" opacity="0.35"/>
      <path class="light-wave"
            d="M394,0 L598,0 C520,120 430,220 435,330 C440,440 560,470 570,580 C580,700 520,820 442,980 L236,980 C270,900 365,830 380,720 C400,600 310,560 290,420 C260,230 330,110 394,0 Z"
            fill="var(--blush)"/>
      <path class="left-panel"
            d="M0,0 L394,0 C330,110 260,230 290,420 C310,560 400,600 380,720 C365,830 270,900 236,980 L0,980 Z"
            fill="var(--rose)"/>
      <rect class="pouch-band" x="30" y="284" width="724" height="414" rx="6" fill="#b8284f" opacity="0.18"/>
      <rect class="pouch-edge-left" x="30" y="284" width="22" height="414" fill="#9e1e44" opacity="0.12"/>
      <rect class="pouch-edge-right" x="732" y="284" width="22" height="414" fill="#9e1e44" opacity="0.12"/>
      <g class="disposal-icons" fill="var(--white)">
        <circle cx="562" cy="240" r="12"/>
        <circle cx="618" cy="240" r="14"/>
        <rect x="642" y="226" width="24" height="28" rx="2"/>
      </g>
      <circle class="brand-dot" cx="206" cy="352" r="20" fill="var(--white)"/>
      <circle class="natural-badge" cx="598" cy="396" r="60" fill="none" stroke="var(--blush)" stroke-width="6"/>
      <circle class="natural-badge-core" cx="598" cy="396" r="52" fill="var(--blush)" opacity="0.35"/>
      <circle class="biodegradable-mark" role="img" aria-label="biodegradable mark with curved label" cx="148" cy="560" r="44" fill="var(--blush)" opacity="0.55"/>
    </svg>

    <div class="text intro">
      <div class="label">Deo wipe for women</div>
      Wet bio deo wipe for that fresh feeling even at the end of the day. Enter your last meeting of the day with a fresh and clean feeling. Fresh yourself with these soft and careful wipes and experience the gentle feeling. For all occasions where you need refreshment. While traveling, working, sporting or just to prepare for your date. Enjoy the fresh life.
    </div>

    <h1 class="brand-name">BRISK<br>TISSU</h1>
    <div class="tagline">ENVIRONMENTAL FRIENDLY WIPES</div>
    <h2 class="product-name"><span class="deo">DEO</span><span class="wipe">WIPE</span></h2>
    <div class="audience">For women</div>

    <div class="text maker">
      <div class="label">BRISK TISSU</div>
      Made in the EU, designed by Brisk Tissu BV, P.O. Box 4120, 7400AB Ravelstad - The Netherlands<br>
      www.briskissu.nl
    </div>
    <div class="text best-before">Best used before the end of:</div>

    <div class="seal-strip"></div>

    <div class="text ingredients">
      <div class="label">Ingredients</div>
      Aqua, Aluminum Chlorohydrate, Propylene Glycol, PEG-40 Hydrogenated Castor Oil, Ethylhexylglycerin, Octenidine HCl, Phenoxyethanol, Parfum, Limonene.
    </div>
  </section>
</body>
</html>
```